Flyer Design Project

I am opening a yoga studio called Willowmere Yoga .Pilates. Fitness
and require a flyer that will be letterbox dropped. It will two sided - DL size.100mm × 210mm

The studio will offer Vinyasa Flow Yoga and Mat Pilates classes. We aim to enable people to lead healthier, happier lives through improved strength, flexibility and general well being that regular yoga and pilates practice offers.

We offer group classes, private and semi private sessions in yoga and pilates.

it must have the logo on it- I have uploaded the logo in two versions - not sure what will look the best.

pick up one of the colours from the logo as the background colour.

Side one:
Simple and clean with one side showing logo and address details, website and with simple intro about studio (if it fits)

Location: 1st Floor, 17 Larkspur Parade, Tindale, 3286
phone: 0428 596143
www.willowmeretindale.com.au

OPENING OCTOBER

other side - class descriptions and intro offer for new clients
$20 for 7 days of classes
$99 for 1 month unlimited.

Class descriptions:
Vinyasa Flow yoga: A class that flows from pose to pose integrating breath, alignment, strength and power. All levels are catered for in a warm room heated to around 26 degrees. You will leave feeling inspired, empowered and energised.

Mat Pilates: A strong, challenging class integrating the key principles of pilates: concentration, control, centring, precision, flowing movement and breath. Using the core as a focus to develop these principles you will be hooked on the physical freedom you experience post workout:improved strength, flexibility and vitality that pilates offers.

Private and semi Private tuition available.

Target Market(s)

mainly women, athletic, 35-55 age, middle class, well educated

Industry/Entity Type

Fitness

Requirements
Must have
• 2 pages
the logo

Should not have
• no pics

```html
<!DOCTYPE html>
<html lang="en">
<head>
<meta charset="utf-8">
<title>Willowmere Yoga – DL Flyer</title>
<link rel="stylesheet" href="https://fonts.googleapis.com/css2?family=Questrial&family=Montserrat:wght@600;700&family=Arimo:wght@400;700&display=swap">
<style>
  :root {
    --canvas: #3a3a3a;
    --panel: #0b0b0b;
    --panel-edge: #1c1c1c;
    --white: #ffffff;
    --text: #e6e6e6;
    --red: #d8141c;
    --red-deep: #7a0508;
    --band: #262626;
    --band-dark: #141414;
  }
  * { margin: 0; padding: 0; box-sizing: border-box; }
  html, body { width: 1200px; height: 928px; overflow: hidden; }
  body {
    background: var(--canvas);
    position: relative;
    font-family: "Arimo", Arial, sans-serif;
    color: var(--text);
  }
  .flyer-side {
    position: absolute;
    top: 95px;
    width: 340px;
    height: 740px;
    background: radial-gradient(ellipse at 70% 60%, #1a1a1a 0%, var(--panel) 65%);
    border: 1px solid var(--panel-edge);
    overflow: hidden;
  }
  .flyer-front { left: 215px; }
  .flyer-back { left: 625px; }

  /* Front */
  .brand-name {
    position: absolute;
    top: 200px; left: 0; right: 0;
    text-align: center;
    font-family: "Questrial", sans-serif;
    font-size: 19px;
    line-height: 1.2;
    color: var(--white);
    white-space: nowrap;
  }
  .opening {
    position: absolute;
    top: 288px; left: 0; right: 0;
    text-align: center;
    font-family: "Questrial", sans-serif;
    font-weight: 400;
    font-size: 29px;
    color: var(--white);
    letter-spacing: 0.5px;
  }
  .intro {
    position: absolute;
    top: 372px; left: 24px; right: 24px;
    text-align: center;
    font-size: 13.4px;
    line-height: 1.55;
    color: var(--text);
  }
  .intro p + p { margin-top: 22px; }
  .contact {
    position: absolute;
    top: 620px; left: 0; right: 0;
    text-align: center;
    font-weight: 700;
    font-size: 13.4px;
    line-height: 1.35;
    color: var(--white);
    font-style: normal;
  }

  /* Back */
  .offers {
    position: absolute;
    top: 36px; left: 0; right: 0;
    display: flex;
  }
  .offer { flex: 1; text-align: center; }
  .offer + .offer { border-left: 1px solid #3a3a3a; }
  .offer-price {
    font-family: "Montserrat", sans-serif;
    font-weight: 700;
    font-size: 66px;
    line-height: 1;
    letter-spacing: -1px;
    background: linear-gradient(180deg, #ff2a2a 0%, var(--red) 45%, var(--red-deep) 100%);
    -webkit-background-clip: text;
    background-clip: text;
    color: transparent;
  }
  .offer-term {
    margin-top: 12px;
    font-family: "Questrial", sans-serif;
    font-size: 21px;
    line-height: 1.15;
    color: var(--white);
  }
  .class-block { position: absolute; left: 0; right: 0; }
  .class-vinyasa { top: 238px; }
  .class-pilates { top: 440px; }
  .class-band {
    position: relative;
    height: 36px;
    margin-left: 6px;
    background: linear-gradient(180deg, var(--band) 0%, var(--band-dark) 100%);
  }
  .class-title {
    position: absolute;
    top: -8px; left: 68px;
    width: 210px; height: 30px;
    border-radius: 4px;
    background: linear-gradient(180deg, #ff3b3b 0%, var(--red) 55%, #a80a10 100%);
    font-family: "Arimo", sans-serif;
    font-weight: 700;
    font-size: 17px;
    line-height: 30px;
    text-align: center;
    color: #1a0000;
  }
  .class-desc {
    margin: 10px 22px 0 22px;
    font-size: 13px;
    line-height: 1.55;
    color: var(--text);
  }
  .tuition-note {
    position: absolute;
    top: 696px; left: 22px; right: 10px;
    font-weight: 700;
    font-size: 13px;
    color: var(--red);
  }
</style>
</head>
<body>

  <section class="flyer-side flyer-front">
    <div class="brand-name">Willowmere Yoga .Pilates. Fitness</div>
    <h1 class="opening">OPENING OCTOBER</h1>
    <div class="intro">
      <p>The studio will offer Vinyasa Flow Yoga and Mat Pilates classes. We aim to enable people to lead healthier, happier lives through improved strength, flexibility and general well being that regular yoga and pilates practice offers.</p>
      <p>We offer group classes, private and semi private sessions in yoga and pilates.</p>
    </div>
    <address class="contact">
      1st Floor, 17 Larkspur Parade<br>
      Tindale, 3286<br>
      0428 596143<br>
      www.willowmeretindale.com.au
    </address>
  </section>

  <section class="flyer-side flyer-back">
    <div class="offers">
      <div class="offer">
        <div class="offer-price">$20</div>
        <div class="offer-term">for 7 days<br>of classes</div>
      </div>
      <div class="offer">
        <div class="offer-price">$99</div>
        <div class="offer-term">1 month<br>unlimited</div>
      </div>
    </div>

    <article class="class-block class-vinyasa">
      <div class="class-band"><h2 class="class-title">Vinyasa Flow Yoga</h2></div>
      <p class="class-desc">A class that flows from pose to pose integrating breath, alignment, strength and power. All levels are catered for in a warm room heated to around 26 degrees. You will leave feeling inspired, empowered and energised.</p>
    </article>

    <article class="class-block class-pilates">
      <div class="class-band"><h2 class="class-title">Mat Pilates</h2></div>
      <p class="class-desc">A strong, challenging class integrating the key principles of pilates: concentration, control, centring, precision, flowing movement and breath. Using the core as a focus to develop these principles you will be hooked on the physical freedom you experience post workout:improved strength, flexibility and vitality that pilates offers.</p>
    </article>

    <p class="tuition-note">Private and semi Private tuition available.</p>
  </section>

</body>
</html>
```